Harbor Rest Company Needs Business Card

Looking for a very nice looking business card. Creative but not extravagant. We sell beds and pillows across the U.S. and need something professional but catchy. I have attached the logo.

Name : Dale Morton
Title : President
Phone : (800) 417-2960
Email: rest@quiltano.com
Website: www.quiltano.com

Can be single-sided or double-sided
horizontal or vertical

Can use Blues/Greys

Target Market(s)

Mass Market

Industry/Entity Type

Retail

Contact Information for Business Card

Name : Dale Morton
Title : President
Phone : (800) 417-2960
Email: rest@quiltano.com
Website: www.quiltano.com

Requirements
Must have
• Clean, Modern, Smooth
• Can use Blues/Greys
• On the other side without the information - have something simple like www.quiltano.com or our logo
Nice to have
• Surprise me
Should not have
• Nothing crazy, nothing cluttered

```html
<!DOCTYPE html>
<html lang="en">
<head>
<meta charset="utf-8">
<title>Harbor Rest Company – Business Card</title>
<link rel="stylesheet" href="https://fonts.googleapis.com/css2?family=Source+Sans+3:wght@300;400;600&display=swap">
<style>
  :root {
    --backdrop: #ebe8e3;
    --kraft-light: #cfae86;
    --kraft-mid: #c19c70;
    --kraft-dark: #ad875b;
    --ink: #1b1712;
  }
  * { box-sizing: border-box; margin: 0; padding: 0; }
  html, body {
    width: 1200px;
    height: 900px;
    overflow: hidden;
    background: var(--backdrop);
    font-family: "Source Sans 3", "Myriad Pro", Arial, sans-serif;
    color: var(--ink);
  }
  .canvas {
    position: relative;
    width: 1200px;
    height: 900px;
  }
  .card {
    position: absolute;
    width: 555px;
    height: 343px;
    background:
      radial-gradient(ellipse at 45% 40%, var(--kraft-light) 0%, var(--kraft-mid) 55%, var(--kraft-dark) 100%);
    box-shadow: 0 6px 18px rgba(60, 45, 25, 0.18);
  }
  .card--front { left: 238px; top: 62px; }
  .card--back  { left: 460px; top: 518px; width: 557px; height: 344px; }

  .contact {
    position: absolute;
    left: 0;
    right: 0;
    top: 102px;
    padding-left: 50px;
    text-align: center;
    line-height: 1.3;
  }
  .contact__name {
    font-size: 19px;
    font-weight: 600;
  }
  .contact__title {
    font-size: 15px;
    font-weight: 400;
  }
  .contact__details {
    margin-top: 26px;
    font-size: 15px;
    font-weight: 400;
    line-height: 20px;
  }

  .brand {
    position: absolute;
    left: 0;
    right: 0;
    top: 122px;
    padding-left: 56px;
    text-align: center;
    font-size: 76px;
    font-weight: 300;
    letter-spacing: 2px;
    line-height: 1;
  }
</style>
</head>
<body>
  <main class="canvas">
    <section class="card card--front" aria-label="Business card, contact side">
      <div class="contact">
        <p class="contact__name">Dale Morton</p>
        <p class="contact__title">President</p>
        <div class="contact__details">
          <p class="contact__phone">(800) 417-2960</p>
          <p class="contact__email">rest@quiltano.com</p>
          <p class="contact__web">www.quiltano.com</p>
        </div>
      </div>
    </section>

    <section class="card card--back" aria-label="Business card, brand side">
      <p class="brand">quiltano</p>
    </section>
  </main>
</body>
</html>
```